Mezzanine Floor Manufacturer looking for a new business card design

We manufacture mezzanine floors and are providers of racking systems. We provide a range of items/services - simple rack repairs , full warehouse fit outs , manufacturer and install mezzanine floors , partitioning and large turnkey projects. Recently had a new website - www.corvane-shelving.co.uk and would like our business cards updating aswell . Our current card is single sided in the old logo colours (pdf attached) and needs updating.

Target Market(s)

We deal with large projects/ multi national companies and also smaller projects and companies throughout the UK ranging from a single warehouse to a large multi site company.

Industry/Entity Type

Business

Contact Information for Business Card

Will have job title,tel no's, email ,website address etc like example pdf

Requirements
Must have
• Hi - needs to use the colours of the logo & new website. Card needs to be professional

```html
<!DOCTYPE html>
<html lang="en">
<head>
<meta charset="utf-8">
<title>Corvane Business Card</title>
<link href="https://fonts.googleapis.com/css2?family=Open+Sans:wght@400;600;700&display=swap" rel="stylesheet">
<style>
  :root {
    --brand-red: #d3202a;
    --ink: #4a4a4a;
    --ink-dark: #3c3c3c;
    --card: #ffffff;
    --backdrop: #2b2b2b;
  }
  * { box-sizing: border-box; margin: 0; padding: 0; }
  html, body {
    width: 1200px; height: 900px; overflow: hidden;
    background: var(--backdrop);
    font-family: "Open Sans", sans-serif;
    color: var(--ink);
  }
  .canvas {
    width: 1200px; height: 900px;
    display: flex; flex-direction: column; align-items: center; justify-content: center;
    gap: 40px;
  }
  .card {
    position: relative;
    width: 620px; height: 400px;
    background: var(--card);
    border-radius: 22px;
    overflow: hidden;
  }

  /* Front */
  .brand-block { position: absolute; left: 48px; top: 92px; }
  .brand-mark { display: flex; align-items: center; gap: 14px; }
  .brand-dot { width: 58px; height: 58px; border-radius: 50%; background: var(--brand-red); }
  .brand-name { font-weight: 700; font-size: 50px; letter-spacing: 3px; color: var(--brand-red); line-height: 1; }
  .front-web { margin-top: 22px; font-size: 17px; letter-spacing: 1px; color: var(--ink); }
  .front-web .accent { color: var(--brand-red); }

  .services {
    position: absolute; right: 40px; bottom: 62px;
    text-align: right; list-style: none;
    font-size: 14px; font-weight: 600; letter-spacing: 1px; line-height: 1.55;
    text-transform: uppercase; color: var(--ink);
  }
  .services .heading { color: var(--brand-red); font-weight: 700; font-size: 16px; padding-right: 20px; }
  .services li.item { position: relative; padding-right: 20px; }
  .services li.item::after {
    content: ""; position: absolute; right: 0; top: 50%;
    width: 9px; height: 9px; margin-top: -4px; border-radius: 50%; background: var(--brand-red);
  }
  .services li.plain { padding-right: 20px; }

  /* Back */
  .side-tab { position: absolute; left: 0; top: 104px; width: 12px; height: 44px; background: var(--brand-red); border-radius: 0 4px 4px 0; }
  .person { position: absolute; left: 42px; top: 92px; }
  .person-name { font-size: 27px; font-weight: 700; letter-spacing: 1px; color: var(--ink-dark); line-height: 1.1; }
  .person-role { font-size: 15px; font-weight: 600; letter-spacing: 1px; color: var(--brand-red); margin-top: 2px; }
  .address { margin-top: 8px; font-size: 15px; line-height: 1.35; color: var(--ink); letter-spacing: 0.5px; }

  .back-brand { position: absolute; right: 44px; top: 70px; display: flex; flex-direction: column; align-items: flex-end; gap: 16px; }
  .back-brand .brand-name { font-size: 44px; }
  .back-brand .brand-dot { width: 50px; height: 50px; }

  .contacts { position: absolute; left: 42px; bottom: 36px; list-style: none; font-size: 15px; line-height: 1.45; letter-spacing: 0.5px; color: var(--ink); }
  .contacts li { display: flex; align-items: center; gap: 12px; }
  .contacts svg { width: 13px; height: 13px; fill: var(--brand-red); flex: none; }
</style>
</head>
<body>
<main class="canvas">

  <section class="card card-front" aria-label="Card front">
    <div class="brand-block">
      <div class="brand-mark">
        <span class="brand-dot"></span>
        <span class="brand-name">CORVANE</span>
      </div>
      <p class="front-web">www.<span class="accent">corvane-shelving</span>.co.uk</p>
    </div>
    <ul class="services">
      <li class="heading">Services</li>
      <li class="item">Rack Repairs</li>
      <li class="item">Full Warehouse Fit Outs</li>
      <li class="item">Manufacturer and Install Mezzanine Floors</li>
      <li class="item">Partitioning and Large Turnkey Projects.</li>
    </ul>
  </section>

  <section class="card card-back" aria-label="Card back">
    <span class="side-tab"></span>
    <div class="person">
      <h1 class="person-name">DEAN WHITLOCK</h1>
      <p class="person-role">TECHNICAL SALES</p>
      <p class="address">Nine Willow Close<br>Harland Gate Business Park<br>Ashby, Leicestershire LE9 4QT</p>
    </div>

    <div class="back-brand">
      <span class="brand-dot"></span>
      <span class="brand-name">CORVANE</span>
    </div>

    <ul class="contacts">
      <li><svg viewBox="0 0 24 24"><path d="M6.6 10.8a15.1 15.1 0 0 0 6.6 6.6l2.2-2.2c.3-.3.7-.4 1-.2 1.1.4 2.3.6 3.6.6.6 0 1 .4 1 1V20c0 .6-.4 1-1 1A17 17 0 0 1 3 4c0-.6.4-1 1-1h3.5c.6 0 1 .4 1 1 0 1.3.2 2.5.6 3.6.1.3 0 .7-.2 1z"/></svg>01632 960418</li>
      <li><svg viewBox="0 0 24 24"><path d="M7 1h10a2 2 0 0 1 2 2v18a2 2 0 0 1-2 2H7a2 2 0 0 1-2-2V3a2 2 0 0 1 2-2zm0 3v14h10V4zm5 15.5a1.2 1.2 0 1 0 0 2.4 1.2 1.2 0 0 0 0-2.4z"/></svg>07700 900342</li>
      <li><svg viewBox="0 0 24 24"><path d="M6 2h9l3 3v5h2a2 2 0 0 1 2 2v8a2 2 0 0 1-2 2H4a2 2 0 0 1-2-2v-8a2 2 0 0 1 2-2h2zm2 2v6h8V6h-2V4zm-1 10v2h2v-2zm4 0v2h2v-2zm4 0v2h2v-2z"/></svg>01632 960577</li>
      <li><svg viewBox="0 0 24 24"><path d="M2 5h20v14H2zm2 2v.5l8 5 8-5V7zm0 2.9V17h16V9.9l-8 5z"/></svg>dean@corvane-shelving.co.uk</li>
      <li><svg viewBox="0 0 24 24"><path d="M12 2a10 10 0 1 0 0 20 10 10 0 0 0 0-20zm6.9 9h-3a15 15 0 0 0-1.3-5.6A8 8 0 0 1 18.9 11zM12 4.1c.9 1.2 1.7 3.6 1.9 6.9h-3.8c.2-3.3 1-5.7 1.9-6.9zM9.4 5.4A15 15 0 0 0 8.1 11h-3a8 8 0 0 1 4.3-5.6zM5.1 13h3a15 15 0 0 0 1.3 5.6A8 8 0 0 1 5.1 13zm6.9 6.9c-.9-1.2-1.7-3.6-1.9-6.9h3.8c-.2 3.3-1 5.7-1.9 6.9zm2.6-1.3a15 15 0 0 0 1.3-5.6h3a8 8 0 0 1-4.3 5.6z"/></svg>www.corvane-shelving.co.uk</li>
    </ul>
  </section>

</main>
</body>
</html>
```